Barrister Letterhead incorporating existing logo/design

Require new letterhead template to incorporate logo and information on 'Letter 2015' word document. Currently the information on the letterhead is very busy and would like a cleaner look.
Must look good in black and white, and colour when printed.

Target Market(s)

Professional

Industry/Entity Type

Legal

Requirements
Must have
• Clean professional look.

```html
<!DOCTYPE html>
<html lang="en">
<head>
<meta charset="utf-8">
<title>Harlow Chambers Letterhead</title>
<link href="https://fonts.googleapis.com/css2?family=Cinzel:wght@700;900&family=Questrial&family=Roboto+Slab:wght@900&display=swap" rel="stylesheet">
<style>
  :root{
    --band-top:#1450d6;
    --band-bottom:#0c2563;
    --band-mid:#1239a0;
    --mark:#1c2b57;
    --ink-light:#ffffff;
    --footer-ink:#10205a;
    --pattern:#8fb0f0;
    --faint:#efefef;
    --paper:#ffffff;
  }
  *{margin:0;padding:0;box-sizing:border-box}
  html,body{width:1200px;height:1000px;overflow:hidden;background:var(--paper)}
  .sheet-set{display:flex;width:1200px;height:1000px;gap:2px;background:#dcdcdc}
  .letterhead{position:relative;width:599px;height:1000px;background:var(--paper);overflow:hidden}
  .letterhead--mono{
    --band-top:#6a6a6a;--band-bottom:#2e2e2e;--band-mid:#4a4a4a;
    --mark:#2a2a2a;--footer-ink:#1a1a1a;--pattern:#b8b8b8;
  }

  .header-band{position:absolute;left:0;top:0;width:100%;height:105px;
    background:linear-gradient(180deg,var(--band-top),var(--band-bottom))}
  .barrister-details{position:absolute;right:300px;top:18px;text-align:right;
    font-family:"Cinzel",serif;font-weight:900;color:var(--ink-light);
    font-size:13.5px;letter-spacing:2px;line-height:17.5px}
  .contact-line{position:absolute;left:122px;font-family:"Questrial",sans-serif;
    color:var(--ink-light);font-size:11.5px;white-space:nowrap}
  .contact-line--email{top:70px;letter-spacing:6.6px}
  .contact-line--web{top:89px;letter-spacing:7.4px}

  .chambers-tag{position:absolute;left:310px;top:18px;width:280px;height:45px;
    background:var(--paper);border:2px solid var(--mark);display:flex;align-items:center;gap:10px;padding-left:8px}
  .chambers-tag__square{width:28px;height:28px;background:var(--mark)}
  .chambers-tag__name{font-family:"Cinzel",serif;font-weight:700;font-size:19px;color:var(--mark);letter-spacing:0.5px}

  .corner-square{position:absolute;left:20px;top:62px;width:87px;height:76px;
    background:var(--mark);border:3px solid var(--paper);outline:1px solid var(--mark)}

  .watermark{position:absolute;inset:0}
  .fleur{position:absolute;background:radial-gradient(ellipse at center,#f0f0f0 55%,rgba(240,240,240,0) 72%)}
  .fleur--upper{left:40px;top:110px;width:220px;height:230px}
  .fleur--lower{left:365px;top:660px;width:220px;height:230px}
  .watermark-square{position:absolute;left:105px;top:300px;width:400px;height:400px;
    transform:rotate(-24deg);border:14px solid var(--faint);outline:6px solid var(--faint);outline-offset:6px}
  .watermark-square__fill{position:absolute;inset:10px;background:var(--faint)}

  .footer-band{position:absolute;left:0;top:895px;width:100%;height:105px;
    background:linear-gradient(180deg,var(--band-mid),var(--band-bottom))}
  .footer-pattern{position:absolute;left:0;top:0;width:100%;height:12px;
    background:linear-gradient(180deg,var(--pattern),var(--band-top))}
  .footer-address{position:absolute;left:120px;top:15px;width:312px;height:68px;background:var(--paper);
    text-align:center;font-family:"Roboto Slab",serif;font-weight:900;font-size:10.5px;line-height:13.2px;
    color:var(--footer-ink);padding-top:2px}
  .footer-tag{position:absolute;left:440px;top:44px;width:148px;height:40px;background:var(--paper);
    display:flex;align-items:center;gap:6px;padding-left:6px}
  .footer-tag__square{width:28px;height:28px;background:var(--mark)}
  .footer-tag__name{font-family:"Cinzel",serif;font-weight:700;font-size:13px;line-height:15px;color:var(--mark)}
</style>
</head>
<body>
<main class="sheet-set">
  <section class="letterhead">
    <div class="watermark">
      <div class="fleur fleur--upper" role="img" aria-label="Faint fleur-de-lis ornament"></div>
      <div class="watermark-square"><div class="watermark-square__fill"></div></div>
      <div class="fleur fleur--lower" role="img" aria-label="Faint fleur-de-lis ornament"></div>
    </div>
    <header class="header-band">
      <div class="barrister-details">ELLIOT MARSH LL.B.<br>BARRISTER-AT-LAW<br>ABN 12 345 678 901</div>
      <div class="chambers-tag"><span class="chambers-tag__square"></span><span class="chambers-tag__name">HARLOW CHAMBERS</span></div>
      <div class="contact-line contact-line--email">Email emarsh@kingsbar.org.au</div>
      <div class="contact-line contact-line--web">www.harlowchambers.com.au</div>
    </header>
    <div class="corner-square"></div>
    <footer class="footer-band">
      <div class="footer-pattern" role="img" aria-label="Decorative scroll border"></div>
      <div class="footer-address">HARLOW CHAMBERS<br>LEVEL 2 14 HARLOW STREET, KINGSPORT<br>P.O. BOX 812, KINGSPORT. Q. 4800<br>TELEPHONE 07 5550 0142<br>FAX 07 5550 0187</div>
      <div class="footer-tag"><span class="footer-tag__square"></span><span class="footer-tag__name">HARLOW<br>CHAMBERS</span></div>
    </footer>
  </section>

  <section class="letterhead letterhead--mono">
    <div class="watermark">
      <div class="fleur fleur--upper" role="img" aria-label="Faint fleur-de-lis ornament"></div>
      <div class="watermark-square"><div class="watermark-square__fill"></div></div>
      <div class="fleur fleur--lower" role="img" aria-label="Faint fleur-de-lis ornament"></div>
    </div>
    <header class="header-band">
      <div class="barrister-details">ELLIOT MARSH LL.B.<br>BARRISTER-AT-LAW<br>ABN 12 345 678 901</div>
      <div class="chambers-tag"><span class="chambers-tag__square"></span><span class="chambers-tag__name">HARLOW CHAMBERS</span></div>
      <div class="contact-line contact-line--email">Email emarsh@kingsbar.org.au</div>
      <div class="contact-line contact-line--web">www.harlowchambers.com.au</div>
    </header>
    <div class="corner-square"></div>
    <footer class="footer-band">
      <div class="footer-pattern" role="img" aria-label="Decorative scroll border"></div>
      <div class="footer-address">HARLOW CHAMBERS<br>LEVEL 2 14 HARLOW STREET, KINGSPORT<br>P.O. BOX 812, KINGSPORT. Q. 4800<br>TELEPHONE 07 5550 0142<br>FAX 07 5550 0187</div>
      <div class="footer-tag"><span class="footer-tag__square"></span><span class="footer-tag__name">HARLOW<br>CHAMBERS</span></div>
    </footer>
  </section>
</main>
</body>
</html>
```